family chiropractic health care team needs a modern business card design

Healthcare office with Chiropractors, Physiotherapists, Massage therapists and possibly other practitioners in the future. This is a friendly family office with patients of all ages (and lots of kids) that just moved into a new larger modern office.
Look at the website for photos of the office.
Design for the front and back of a business card required.
Text for the front:
Office logo and name of the office:
Bright Path Wellness Centre
Name of current Practitioner:
Dr. Marten Quovel B.Sc., D.C. Chiropractor
(But please include options to swap out name and title for other practitioners )

address:
218 Farrow Gate
Etobicoke ON.
K2J 6P4
Phone: 416-872-0196 (PATH)
Web site and email:
www.brightpathwellnesscentre.example
brightpathchiro@mailbox.example

2 versions of the back of the card:
1. text below
2. appointment schedule card

Text on back of card:
Chiropractic Card text on back of the card:
There is more to chiropractic than the relief of headaches and back pain! Our primary focus is the integrity of your nerve system, which controls and regulates every cell and tissue of your body. The moving bones of the spinal column can impair this vital communication link between your brain and body. We help improve the function and structure of your spine, reducing nerve system compromise. The result?
Even non-spinal related health problems can show improvement
without drugs
without surgery
regardless of age
for over a century
naturally

Appointment Card info For Back:
Please integrate design elements from the front of the card into an appointment card format.
M Tu W Th F Sat (and a line for writing on beside each one)

```html
<!DOCTYPE html>
<html lang="en">
<head>
<meta charset="utf-8">
<title>Bright Path Wellness Centre – Business Card</title>
<link rel="stylesheet" href="https://fonts.googleapis.com/css2?family=EB+Garamond:wght@400;600;700&display=swap">
<style>
  :root {
    --green: #97c156;
    --grey: #808080;
    --white: #ffffff;
    --backdrop: #eef0ec;
    --silver-dark: #5c5c5c;
    --silver-light: #e6e6e6;
    --serif: "EB Garamond", Georgia, serif;
  }
  html, body {
    margin: 0;
    padding: 0;
    width: 1200px;
    height: 1200px;
    overflow: hidden;
    background: var(--backdrop);
    font-family: var(--serif);
  }
  .card {
    position: absolute;
    left: 170px;
    width: 860px;
    height: 503px;
    background: var(--white);
    overflow: hidden;
  }
  .card--front { top: 79px; }
  .card--back { top: 627px; }

  .brand-name {
    position: absolute;
    left: 0;
    width: 100%;
    margin: 0;
    text-align: center;
    white-space: nowrap;
    color: var(--green);
    font-family: var(--serif);
    font-weight: 600;
    font-size: 54px;
    line-height: 1;
  }
  .card--front .brand-name { top: 110px; }
  .card--back .brand-name { top: 224px; }

  .stripe {
    position: absolute;
    left: 0;
    width: 100%;
    display: flex;
  }
  .card--front .stripe { top: 252px; height: 24px; }
  .card--back .stripe { top: 412px; height: 23px; }
  .stripe__accent { width: 328px; }
  .stripe__rest { flex: 1; background: var(--grey); }
  .card--front .stripe__accent {
    background: linear-gradient(90deg,
      var(--silver-dark) 0%, var(--silver-light) 25%, var(--silver-dark) 50%,
      var(--silver-light) 75%, var(--silver-dark) 100%);
  }
  .card--back .stripe__accent { background: var(--green); }

  .info-panel {
    position: absolute;
    left: 0;
    top: 276px;
    width: 100%;
    height: 227px;
    background: var(--green);
    color: var(--white);
  }
  .practitioner {
    position: absolute;
    left: 53px;
    top: 22px;
  }
  .practitioner__name {
    margin: 0;
    font-size: 25px;
    font-weight: 700;
    letter-spacing: 0.5px;
    line-height: 1.1;
  }
  .practitioner__credentials {
    margin: 2px 0 0;
    font-size: 16px;
  }
  .practitioner__title {
    margin: 4px 0 0;
    font-size: 20px;
  }
  .contact {
    position: absolute;
    right: 38px;
    top: 36px;
    margin: 0;
    padding: 0;
    list-style: none;
    text-align: right;
  }
  .contact__item {
    display: flex;
    justify-content: flex-end;
    align-items: center;
    gap: 12px;
    font-size: 19px;
    height: 24px;
    margin-bottom: 13px;
    white-space: nowrap;
  }
  .contact__item--address { margin-top: 8px; }
  .contact__icon {
    width: 14px;
    height: 14px;
    flex: none;
  }
</style>
</head>
<body>

<section class="card card--front" aria-label="Business card front">
  <p class="brand-name">Bright Path Wellness Centre</p>

  <div class="stripe">
    <span class="stripe__accent"></span>
    <span class="stripe__rest"></span>
  </div>

  <div class="info-panel">
    <div class="practitioner">
      <p class="practitioner__name">DR. MARTEN QUOVEL</p>
      <p class="practitioner__credentials">B.Sc., D.C. Chiropractor</p>
      <p class="practitioner__title">Business Development Manager</p>
    </div>

    <ul class="contact">
      <li class="contact__item">416-872-0196 (PATH)
        <svg class="contact__icon" viewBox="0 0 16 16" aria-hidden="true">
          <path d="M4 1.5l2.2 3-1.4 1.6c.8 1.9 2.3 3.4 4.2 4.2l1.6-1.4 3 2.2-1.1 2.6C7.3 13.4 2.6 8.7 1.4 3.4z" fill="#fff"/>
        </svg>
      </li>
      <li class="contact__item">www.brightpathwellnesscentre.example
        <svg class="contact__icon" viewBox="0 0 16 16" aria-hidden="true">
          <rect x="1.5" y="3.5" width="13" height="9" rx="1" fill="#fff"/>
          <path d="M1.8 4l6.2 4.6L14.2 4" fill="none" stroke="#97c156" stroke-width="1.2"/>
        </svg>
      </li>
      <li class="contact__item">brightpathchiro@mailbox.example
        <svg class="contact__icon" viewBox="0 0 16 16" aria-hidden="true">
          <circle cx="8" cy="8" r="6.5" fill="none" stroke="#fff" stroke-width="1.4"/>
          <ellipse cx="8" cy="8" rx="2.6" ry="6.5" fill="none" stroke="#fff" stroke-width="1.2"/>
          <path d="M1.5 8h13" stroke="#fff" stroke-width="1.2"/>
        </svg>
      </li>
      <li class="contact__item contact__item--address">218 Farrow Gate, Etobicoke ON., K2J 6P4
        <svg class="contact__icon" viewBox="0 0 16 16" aria-hidden="true">
          <path d="M8 1a4.5 4.5 0 0 0-4.5 4.5C3.5 9 8 13 8 13s4.5-4 4.5-7.5A4.5 4.5 0 0 0 8 1z" fill="#fff"/>
          <circle cx="8" cy="5.5" r="1.6" fill="#97c156"/>
          <path d="M3 15h10" stroke="#fff" stroke-width="1.4"/>
        </svg>
      </li>
    </ul>
  </div>
</section>

<section class="card card--back" aria-label="Business card back">
  <p class="brand-name">Bright Path Wellness Centre</p>

  <div class="stripe">
    <span class="stripe__accent"></span>
    <span class="stripe__rest"></span>
  </div>
</section>

</body>
</html>
```